Lounge Night Poster

We need an attractive poster for our new lounge/night club in San Francisco called Velvora Nightclub, promoting our new event, "Lantern Drift". We will have a live band and Asian singers performing during the night. It is like a lounge where people can chill and have a sip. It will open on July 21.

Industry/Entity Type

Club

```html
<!DOCTYPE html>
<html lang="en">
<head>
<meta charset="utf-8">
<title>Lantern Drift – Velvora Nightclub Poster</title>
<link rel="stylesheet" href="https://fonts.googleapis.com/css2?family=Open+Sans:wdth,wght@75..100,400..800&family=Libre+Baskerville:wght@400;700&display=swap">
<style>
  :root {
    --page-bg: #dfe5ea;
    --sky-top: #1b8fd0;
    --sky-mid: #3f3fae;
    --violet: #5a2d92;
    --plum: #3a1c5c;
    --ink: #050505;
    --white: #ffffff;
  }
  * { margin: 0; padding: 0; box-sizing: border-box; }
  html, body {
    width: 1200px; height: 1000px; overflow: hidden;
    background: var(--page-bg);
  }
  .poster {
    position: absolute; left: 303px; top: 38px;
    width: 607px; height: 910px; overflow: hidden;
    color: var(--white);
  }
  .poster-backdrop {
    position: absolute; inset: 0;
    background:
      radial-gradient(ellipse 60% 35% at 55% 8%, rgba(120,210,255,.55), transparent 70%),
      linear-gradient(180deg, var(--sky-top) 0%, #2d6cc4 22%, var(--sky-mid) 42%, var(--violet) 68%, var(--plum) 100%);
  }
  .stage-art {
    position: absolute; left: 410px; top: 340px; width: 197px; height: 260px;
    background: radial-gradient(ellipse at 40% 40%, rgba(230,170,220,.5), rgba(140,80,170,.12) 60%, transparent 75%);
  }
  .band-art {
    position: absolute; left: 0; top: 560px; width: 607px; height: 220px;
    background: linear-gradient(180deg, transparent, rgba(40,20,60,.45) 55%, transparent);
  }
  .text { position: absolute; left: 0; width: 100%; text-align: center; white-space: nowrap; }
  .club-name {
    font-family: "Open Sans", sans-serif; font-weight: 800; font-stretch: 75%;
    line-height: 1; color: var(--white);
  }
  .club-name-main { top: 55px; font-size: 78px; letter-spacing: 1px; }
  .club-name-sub { top: 148px; font-size: 50px; letter-spacing: 6px; }
  .city {
    top: 300px;
    font-family: "Libre Baskerville", serif; font-size: 31px; line-height: 1; letter-spacing: 1px;
  }
  .state {
    top: 348px;
    font-family: "Libre Baskerville", serif; font-size: 14px; letter-spacing: 1px;
  }
  .state::before {
    content: ""; position: absolute; left: 240px; right: 240px; top: -5px;
    border-top: 1px solid rgba(255,255,255,.8);
  }
  .event-title {
    top: 382px;
    font-family: "Open Sans", sans-serif; font-weight: 800; font-stretch: 75%;
    font-size: 108px; line-height: .9; color: var(--ink); letter-spacing: -1px;
  }
  .live-band {
    top: 592px;
    font-family: "Libre Baskerville", serif; font-size: 44px; line-height: 1;
  }
  .singers {
    top: 645px;
    font-family: "Libre Baskerville", serif; font-size: 15px; letter-spacing: .3px;
  }
  .date-badge {
    position: absolute; left: 246px; top: 668px; width: 112px; height: 112px;
    border-radius: 50%; background: var(--ink);
    font-family: "Libre Baskerville", serif; text-align: center;
  }
  .date-day { display: block; font-size: 44px; line-height: 1; padding-top: 14px; }
  .date-month { display: block; font-size: 21px; line-height: 1; margin-top: 6px; }
  .tagline {
    top: 792px;
    font-family: "Libre Baskerville", serif; font-size: 36px; line-height: 1;
  }
</style>
</head>
<body>
  <main class="poster">
    <div class="poster-backdrop" role="img" aria-label="Blue to violet background with soft bokeh lights"></div>
    <div class="stage-art" role="img" aria-label="Hand holding a vintage microphone with sparkles"></div>
    <div class="band-art" role="img" aria-label="Silhouettes of a live band on stage"></div>

    <h1 class="text club-name club-name-main">VELVORA</h1>
    <p class="text club-name club-name-sub">NIGHTCLUB</p>

    <p class="text city">SAN FRANCISCO</p>
    <p class="text state">CALIFORNIA</p>

    <h2 class="text event-title">LANTERN<br>DRIFT</h2>

    <p class="text live-band">LIVE BAND</p>
    <p class="text singers">ASIAN SINGERS PERFORMING</p>

    <div class="date-badge">
      <span class="date-day">21</span>
      <span class="date-month">JULY</span>
    </div>

    <p class="text tagline">CHILL AND HAVE A SIP</p>
  </main>
</body>
</html>
```